Birch Spire Kilo Marsh website

we need a website to cater to 2 aspect of the business. We have Birch spire residence and birch spire office. For the office, we will get their inquire and arrange a face to face meetup to show them the office area for rent. For the residence side, it will need to be like stayrio or velupa.com. we want to allow them to book online for the date they need. We have a total of 10 different room configurations starting at $70 per night and up depending on the size of the room. example of the design is https://lumbrahaven.com/

Target Market(s)

the website should have detail information on the layout, designs, and luxury of the building.

Industry/Entity Type

office and service appartment rental/lease

Coding

Coded - Design and coding required

Number of Pages Required

5+ page

Requirements
Must have
• a luxury perspective
Nice to have
• example https://lumbrahaven.com/

```html
<!DOCTYPE html>
<html lang="en">
<head>
<meta charset="utf-8">
<title>Birch Spire Kilo Marsh — Premium Tower Rentals</title>
<link href="https://fonts.googleapis.com/css2?family=DM+Serif+Display&family=Poppins:wght@400;500;600&display=swap" rel="stylesheet">
<style>
:root{
  --gold:#c9a14a;
  --gold-soft:#d9b66a;
  --ink:#1b1b1b;
  --dark:#161616;
  --panel:#222;
  --text:#444;
  --muted:#777;
  --light:#f4f4f4;
  --white:#fff;
  --sky-top:#dfe8f1;
  --sky-mid:#c6d4e2;
  --link:#2a6fd6;
}
*{margin:0;padding:0;box-sizing:border-box}
html,body{width:1200px;height:5340px;overflow:hidden}
body{font-family:"Poppins",sans-serif;color:var(--text);background:var(--white);position:relative;font-size:13px;line-height:1.6}
.serif{font-family:"DM Serif Display",serif;font-weight:400}
section,header,footer{position:absolute;left:0;width:1200px}
.abs{position:absolute}
.btn{display:inline-block;font-size:11px;font-weight:600;letter-spacing:1px;text-transform:uppercase;padding:10px 28px;text-align:center}
.btn-gold{background:var(--gold);color:var(--ink)}
.btn-dark{background:var(--ink);color:var(--white)}
.eyebrow{font-size:12px;font-weight:600;letter-spacing:1.5px;text-transform:uppercase;color:var(--gold)}
.ph{display:block}

/* header + hero */
.site-header{top:0;height:96px;z-index:3}
.nav{position:absolute;top:16px;display:flex;gap:34px;font-size:11px;font-weight:500;text-transform:uppercase;color:var(--ink)}
.nav-left{left:120px}
.nav-left .active{border-bottom:2px solid var(--ink)}
.nav-right{left:760px;align-items:center}
.brand{position:absolute;left:520px;top:0;width:160px;height:84px;background:var(--ink);display:flex;flex-direction:column;align-items:center;justify-content:center;gap:6px}
.brand-mark{width:14px;height:14px;border:2px solid var(--gold)}
.brand-name{font-family:"DM Serif Display",serif;color:var(--gold);font-size:13px;text-align:center;line-height:1.2}
.hero{top:0;height:770px;background:linear-gradient(180deg,var(--sky-top),#eef3f7 40%,var(--sky-mid) 70%,#8ea4b8)}
.hero-city{position:absolute;left:0;top:360px;width:1200px;height:400px;background:linear-gradient(180deg,rgba(120,140,160,0),#7d8fa3 40%,#5c6d7e 85%,#4c6a3e)}
.hero-title{position:absolute;top:120px;width:100%;text-align:center;font-size:52px;line-height:1.1;color:var(--ink)}
.hero-sub{position:absolute;top:254px;width:100%;text-align:center;font-size:11px;color:var(--text)}
.hero .btn{position:absolute;left:540px;top:302px;width:120px}
.search-panel{position:absolute;left:120px;top:580px;width:952px;height:188px;background:var(--white);box-shadow:0 6px 24px rgba(0,0,0,.12)}
.tab{position:absolute;width:172px;height:40px;border:1px solid var(--ink);font-family:"DM Serif Display",serif;font-size:15px;display:flex;align-items:center;justify-content:center;color:var(--ink)}
.tab.on{background:var(--ink);color:var(--gold)}
.field{position:absolute;height:34px;border:1px solid #ccc;font-size:10px;color:var(--muted);padding:0 10px;display:flex;align-items:center;justify-content:space-between}
.search-panel .btn{position:absolute;left:480px;top:110px;padding:8px 20px}

/* about */
.about{top:860px;height:500px}
.about-tall{left:124px;top:10px;width:196px;height:344px;background:linear-gradient(180deg,#2b3948,#7a8ea4 60%,#1f2a36)}
.about-top{left:448px;top:10px;width:224px;height:196px;background:linear-gradient(160deg,#c7c2b8,#6d5a4c 60%,#2c2420)}
.about-bot{left:448px;top:250px;width:224px;height:200px;background:linear-gradient(160deg,#3a3f46,#8d9099 60%,#22272d)}
.about-badge{left:372px;top:214px;width:92px;height:92px;background:var(--ink);border:3px solid var(--white);display:flex;align-items:center;justify-content:center}
.about-text{left:720px;top:28px;width:340px}
.about-text h2{font-size:44px;line-height:1.05;color:var(--ink);margin:8px 0 20px}
.about-text p{font-size:11px;margin-bottom:14px}

/* residence */
.residence{top:1428px;height:772px;background:var(--dark);color:#cfcfcf}
.center-head{position:absolute;top:90px;width:100%;text-align:center}
.center-head h2{font-size:44px;color:var(--white);margin:4px 0 10px}
.center-head p{font-size:11px;width:560px;margin:0 auto}
.card{position:absolute;width:224px;height:340px;overflow:hidden}
.card .ph{width:100%;height:100%}
.price{position:absolute;right:12px;top:14px;background:var(--gold);color:var(--ink);font-size:10px;font-weight:600;padding:4px 8px}
.card-title{position:absolute;left:16px;bottom:18px;color:var(--white);font-size:22px;line-height:1.05}
.card-arrow{position:absolute;right:14px;bottom:20px;width:34px;height:34px;border-radius:50%;background:rgba(255,255,255,.9);display:flex;align-items:center;justify-content:center}
.slide-arrow{position:absolute;width:28px;height:28px;background:var(--gold);display:flex;align-items:center;justify-content:center}
.residence .btn{position:absolute;left:540px;top:636px;width:120px}

/* office */
.office{top:2200px;height:940px;background:linear-gradient(180deg,var(--white) 60%,#dfe6ed)}
.office-head{position:absolute;left:120px;top:90px;width:620px}
.office-head h2{font-size:44px;color:var(--ink);margin:4px 0 10px}
.office-head p{font-size:11px}
.office .btn{position:absolute;left:892px;top:134px;width:180px}
.office-skyline{position:absolute;left:0;top:600px;width:1200px;height:340px;background:linear-gradient(180deg,rgba(223,230,237,0),#b9c5d2 40%,#8b99a8 85%,#6c7a89)}

/* blog */
.blog{top:3140px;height:780px}
.blog .center-head h2{color:var(--ink)}
.post{position:absolute;top:260px;width:304px}
.post .ph{width:304px;height:200px}
.post-date{font-size:10px;color:var(--gold);font-weight:600;margin:22px 0 6px}
.post h3{font-size:22px;line-height:1.15;color:var(--ink);margin-bottom:12px}
.post p{font-size:11px;margin-bottom:18px}
.read-more{font-size:11px;font-weight:600;color:var(--link);display:flex;align-items:center;gap:10px}

/* testimonials */
.testimonials{top:3920px;height:520px;background:var(--dark);color:#cfcfcf}
.testimonials .office-head h2{color:var(--white)}
.testimonials .btn{position:absolute;left:892px;top:112px;width:180px}
.quote{position:absolute;top:200px;width:304px;height:296px;border:1px solid var(--gold);padding:28px 26px}
.quote-who{display:flex;align-items:center;gap:14px;margin-bottom:18px}
.avatar{width:52px;height:52px;border-radius:50%;background:linear-gradient(160deg,#9bb4c8,#4d6478)}
.quote-name{font-family:"DM Serif Display",serif;color:var(--white);font-size:17px;line-height:1.2}
.quote-role{font-size:10px}
.quote p{font-size:11px;margin-bottom:14px}
.stars{display:flex;gap:4px}

/* partners */
.partners{top:4440px;height:300px;display:flex;align-items:center;justify-content:center;gap:40px}
.partner{width:140px;height:90px;border-radius:8px;background:#e4e4e4}

/* footer */
.site-footer{top:4740px;height:548px;background:var(--dark);color:#cfcfcf}
.foot-col h4{font-family:"DM Serif Display",serif;color:var(--white);font-size:26px;font-weight:400;margin-bottom:22px}
.foot-links{list-style:none;font-size:12px;line-height:2.2}
.foot-divider{position:absolute;top:100px;width:1px;height:300px;background:var(--gold)}
.foot-brand{position:absolute;left:520px;top:170px;width:160px;text-align:center}
.foot-brand .brand-mark{margin:0 auto 10px}
.social{display:flex;justify-content:center;gap:10px;margin-top:18px}
.social span{width:26px;height:26px;border-radius:50%;border:1px solid var(--gold)}
.contact{list-style:none;text-align:right;font-size:12px}
.contact li{display:flex;align-items:center;justify-content:flex-end;gap:14px;margin-bottom:26px}
.contact .ico{width:34px;height:34px;border-radius:50%;background:var(--white);display:flex;align-items:center;justify-content:center;flex:none}
.copyright{position:absolute;top:5288px;left:0;width:1200px;height:52px;display:flex;align-items:center;justify-content:center;font-size:11px;color:var(--text)}
</style>
</head>
<body>

<section class="hero">
  <div class="hero-city" role="img" aria-label="Photograph of a modern city skyline with tall residential towers"></div>
  <h1 class="hero-title serif">Browse Premium Tower<br>Rentals Here</h1>
  <p class="hero-sub">Lorem Ipsum is simply dummy text of the printing and typesetting industry. Lorem Ipsum has been<br>the industry's standard dummy text ever since the 1500s.</p>
  <span class="btn btn-dark">List Now</span>

  <div class="search-panel">
    <div class="tab on" style="left:36px;top:46px">Residential Tower</div>
    <div class="tab" style="left:232px;top:46px">Overnight Stays</div>
    <div class="tab" style="left:36px;top:100px">Offices Tower</div>
    <div class="tab" style="left:232px;top:100px">Day Cab Stays</div>
    <div class="field" style="left:480px;top:14px;width:440px">Enter a location or property</div>
    <div class="field" style="left:480px;top:60px;width:110px">Check in <span>▾</span></div>
    <div class="field" style="left:600px;top:60px;width:110px">Nights <span>▾</span></div>
    <div class="field" style="left:720px;top:60px;width:110px">Rooms <span>▾</span></div>
    <span class="btn btn-gold">Search</span>
  </div>
</section>

<header class="site-header">
  <nav class="nav nav-left"><span class="active">Home</span><span>About Us</span><span>Offices</span><span>Residence</span></nav>
  <div class="brand"><span class="brand-mark"></span><span class="brand-name">Birch Spire<br>Kilo Marsh</span></div>
  <nav class="nav nav-right"><span>Blogs</span><span>Testimonials</span>
    <svg width="14" height="14" viewBox="0 0 14 14"><circle cx="7" cy="5" r="3" fill="none" stroke="#1b1b1b" stroke-width="1.4"/><path d="M1.5 13c1-3 3-4 5.5-4s4.5 1 5.5 4" fill="none" stroke="#1b1b1b" stroke-width="1.4"/></svg>
    <span>Eng ▾</span></nav>
</header>

<section class="about">
  <div class="abs about-tall" role="img" aria-label="Photograph looking up at glass skyscrapers"></div>
  <div class="abs about-top" role="img" aria-label="Photograph of a couple standing in a city street"></div>
  <div class="abs about-bot" role="img" aria-label="Photograph of modern tower facades"></div>
  <div class="abs about-badge"><span class="brand-mark"></span></div>
  <div class="abs about-text">
    <span class="eyebrow">About Us</span>
    <h2 class="serif">Where Sky<br>Meets Comfort</h2>
    <p>Lorem Ipsum is simply dummy text of the printing and typesetting industry. Lorem Ipsum has been the industry's standard dummy text ever since the 1500s, when an unknown printer took a galley of type and scrambled it to make a type specimen book. It has survived not only five centuries, but also the leap into electronic typesetting, remaining essentially unchanged.</p>
    <p>Lorem Ipsum is simply dummy text of the printing and typesetting industry. Lorem Ipsum has been the industry's standard dummy text ever since the 1500s.</p>
    <span class="btn btn-gold" style="margin-top:10px">List Now</span>
  </div>
</section>

<section class="residence">
  <div class="center-head">
    <span class="eyebrow">Birch Spire Residence</span>
    <h2 class="serif">Ascend to Luxury</h2>
    <p>Lorem Ipsum is simply dummy text of the printing and typesetting industry. Lorem Ipsum has been the industry's standard dummy text ever since the 1500s.</p>
  </div>
  <div class="slide-arrow" style="left:76px;top:414px"><svg width="10" height="10" viewBox="0 0 10 10"><path d="M7 1 3 5l4 4" fill="none" stroke="#1b1b1b" stroke-width="1.6"/></svg></div>
  <div class="slide-arrow" style="left:1096px;top:414px"><svg width="10" height="10" viewBox="0 0 10 10"><path d="M3 1l4 4-4 4" fill="none" stroke="#1b1b1b" stroke-width="1.6"/></svg></div>

  <div class="card" style="left:124px;top:252px"><span class="ph" style="height:100%;background:linear-gradient(180deg,#8a7a66,#4a3f34 60%,#1e1a16)" role="img" aria-label="Photograph of a studio apartment interior"></span><span class="price">$29 PER</span><span class="card-title serif">Studio<br>Apartment</span><span class="card-arrow"><svg width="10" height="10" viewBox="0 0 10 10"><path d="M3 1l4 4-4 4" fill="none" stroke="#1b1b1b" stroke-width="1.6"/></svg></span></div>
  <div class="card" style="left:364px;top:252px"><span class="ph" style="height:100%;background:linear-gradient(180deg,#b8ab98,#6a5c4c 60%,#241e18)" role="img" aria-label="Photograph of a luxury apartment living room"></span><span class="price">$29 PER</span><span class="card-title serif">Luxury<br>Apartment</span><span class="card-arrow"><svg width="10" height="10" viewBox="0 0 10 10"><path d="M3 1l4 4-4 4" fill="none" stroke="#1b1b1b" stroke-width="1.6"/></svg></span></div>
  <div class="card" style="left:608px;top:252px"><span class="ph" style="height:100%;background:linear-gradient(180deg,#6a5036,#3b2c1e 60%,#140f0a)" role="img" aria-label="Photograph of a deluxe apartment dining area"></span><span class="price">$29 PER</span><span class="card-title serif">Deluxe<br>Apartment</span><span class="card-arrow"><svg width="10" height="10" viewBox="0 0 10 10"><path d="M3 1l4 4-4 4" fill="none" stroke="#1b1b1b" stroke-width="1.6"/></svg></span></div>
  <div class="card" style="left:852px;top:252px"><span class="ph" style="height:100%;background:linear-gradient(180deg,#9c9484,#5a5246 60%,#1f1c18)" role="img" aria-label="Photograph of a one room apartment bedroom"></span><span class="price">$29 PER</span><span class="card-title serif">One Room<br>Apartment</span><span class="card-arrow"><svg width="10" height="10" viewBox="0 0 10 10"><path d="M3 1l4 4-4 4" fill="none" stroke="#1b1b1b" stroke-width="1.6"/></svg></span></div>

  <span class="btn btn-gold">See All</span>
</section>

<section class="office">
  <div class="office-skyline" role="img" aria-label="Photograph of a hazy city skyline"></div>
  <div class="office-head">
    <span class="eyebrow">Birch Spire Office</span>
    <h2 class="serif">Find Your Perfect Tower Rental</h2>
    <p>Lorem Ipsum is simply dummy text of the printing and typesetting industry. Lorem Ipsum has been the industry's standard dummy text ever since the 1500s.</p>
  </div>
  <span class="btn btn-dark">See All</span>

  <div class="card" style="left:124px;top:260px;height:320px"><span class="ph" style="background:linear-gradient(180deg,#8fa3b3,#4d5e6c 60%,#1f262d)" role="img" aria-label="Photograph of an open plan office"></span><span class="price">$29 PER</span><span class="card-title serif">Dummy<br>Text</span><span class="card-arrow"><svg width="10" height="10" viewBox="0 0 10 10"><path d="M3 1l4 4-4 4" fill="none" stroke="#1b1b1b" stroke-width="1.6"/></svg></span></div>
  <div class="card" style="left:368px;top:260px;height:320px"><span class="ph" style="background:linear-gradient(180deg,#c9c2b6,#7b7264 60%,#2a2620)" role="img" aria-label="Photograph of a bright meeting room"></span><span class="price">$29 PER</span><span class="card-title serif">Dummy<br>Text</span><span class="card-arrow"><svg width="10" height="10" viewBox="0 0 10 10"><path d="M3 1l4 4-4 4" fill="none" stroke="#1b1b1b" stroke-width="1.6"/></svg></span></div>
  <div class="card" style="left:612px;top:260px;height:320px"><span class="ph" style="background:linear-gradient(180deg,#a9b8c2,#5d6c76 60%,#20272c)" role="img" aria-label="Photograph of a glass walled office"></span><span class="price">$29 PER</span><span class="card-title serif">Dummy<br>Text</span><span class="card-arrow"><svg width="10" height="10" viewBox="0 0 10 10"><path d="M3 1l4 4-4 4" fill="none" stroke="#1b1b1b" stroke-width="1.6"/></svg></span></div>
  <div class="card" style="left:856px;top:260px;height:320px"><span class="ph" style="background:linear-gradient(180deg,#d8cc92,#8a7c4a 60%,#2c2816)" role="img" aria-label="Photograph of a coworking office with yellow accents"></span><span class="price">$29 PER</span><span class="card-title serif">Dummy<br>Text</span><span class="card-arrow"><svg width="10" height="10" viewBox="0 0 10 10"><path d="M3 1l4 4-4 4" fill="none" stroke="#1b1b1b" stroke-width="1.6"/></svg></span></div>
  <div class="slide-arrow" style="left:1096px;top:406px"><svg width="10" height="10" viewBox="0 0 10 10"><path d="M3 1l4 4-4 4" fill="none" stroke="#1b1b1b" stroke-width="1.6"/></svg></div>
</section>

<section class="blog">
  <div class="center-head" style="top:80px">
    <span class="eyebrow">Blogs and Latest News</span>
    <h2 class="serif">Begin Your Tower Rental Journey Now</h2>
    <p>Lorem Ipsum is simply dummy text of the printing and typesetting industry. Lorem Ipsum has been the industry's standard dummy text ever since the 1500s.</p>
  </div>
  <article class="post" style="left:120px">
    <span class="ph" style="background:linear-gradient(180deg,#9dc0e0,#3f6f9c 60%,#1c3550)" role="img" aria-label="Photograph of a glass tower against blue sky"></span>
    <div class="post-date">24 May 2024</div>
    <h3 class="serif">Lorem Ipsum is simply dummy text of the printing</h3>
    <p>Lorem Ipsum is simply dummy text of the printing and typesetting industry. Lorem Ipsum has been the industry's standard dummy text ever since the 1500s.</p>
    <span class="read-more">Read more <svg width="28" height="8" viewBox="0 0 28 8"><path d="M0 4h26M22 1l4 3-4 3" fill="none" stroke="#2a6fd6" stroke-width="1.2"/></svg></span>
  </article>
  <article class="post" style="left:446px">
    <span class="ph" style="background:linear-gradient(180deg,#e2a86a,#6a4e3a 55%,#1d1a1c)" role="img" aria-label="Photograph of city towers at sunset"></span>
    <div class="post-date">24 May 2024</div>
    <h3 class="serif">Lorem Ipsum is simply dummy text of the printing</h3>
    <p>Lorem Ipsum is simply dummy text of the printing and typesetting industry. Lorem Ipsum has been the industry's standard dummy text ever since the 1500s.</p>
    <span class="read-more">Read more <svg width="28" height="8" viewBox="0 0 28 8"><path d="M0 4h26M22 1l4 3-4 3" fill="none" stroke="#2a6fd6" stroke-width="1.2"/></svg></span>
  </article>
  <article class="post" style="left:772px">
    <span class="ph" style="background:linear-gradient(180deg,#7fb4e6,#5a7fa3 55%,#2e3e4e)" role="img" aria-label="Photograph of a downtown skyline"></span>
    <div class="post-date">24 May 2024</div>
    <h3 class="serif">Lorem Ipsum is simply dummy text of the printing</h3>
    <p>Lorem Ipsum is simply dummy text of the printing and typesetting industry. Lorem Ipsum has been the industry's standard dummy text ever since the 1500s.</p>
    <span class="read-more">Read more <svg width="28" height="8" viewBox="0 0 28 8"><path d="M0 4h26M22 1l4 3-4 3" fill="none" stroke="#2a6fd6" stroke-width="1.2"/></svg></span>
  </article>
</section>

<section class="testimonials">
  <div class="office-head" style="top:70px">
    <span class="eyebrow">Testimonials</span>
    <h2 class="serif">Reach New Heights</h2>
    <p>Lorem Ipsum is simply dummy text of the printing and typesetting industry. Lorem Ipsum has been the industry's standard dummy text ever since the 1500s.</p>
  </div>
  <span class="btn btn-gold">See All</span>
  <div class="quote" style="left:120px">
    <div class="quote-who"><span class="avatar" role="img" aria-label="Portrait photo of the reviewer"></span><div><div class="quote-name">Nolan Brecker</div><div class="quote-role">Lorem Ipsum</div></div></div>
    <p>Lorem Ipsum is simply dummy text of the printing and typesetting industry. Lorem Ipsum has been the industry's standard dummy text ever since the 1500s, when an unknown printer took a galley of type and scrambled it to make a type specimen book.</p>
    <div class="stars"><svg width="80" height="14" viewBox="0 0 80 14" fill="#c9a14a"><path id="s" d="M7 0l2 4.6 5 .5-3.8 3.3 1.1 5L7 10.8 2.7 13.4l1.1-5L0 5.1l5-.5z"/><use href="#s" x="16"/><use href="#s" x="32"/><use href="#s" x="48"/><use href="#s" x="64"/></svg></div>
  </div>
  <div class="quote" style="left:448px">
    <div class="quote-who"><span class="avatar" role="img" aria-label="Portrait photo of the reviewer" style="background:linear-gradient(160deg,#a89a8a,#4e443a)"></span><div><div class="quote-name">Nolan Brecker</div><div class="quote-role">Lorem Ipsum</div></div></div>
    <p>Lorem Ipsum is simply dummy text of the printing and typesetting industry. Lorem Ipsum has been the industry's standard dummy text ever since the 1500s, when an unknown printer took a galley of type and scrambled it to make a type specimen book.</p>
    <div class="stars"><svg width="80" height="14" viewBox="0 0 80 14" fill="#c9a14a"><use href="#s"/><use href="#s" x="16"/><use href="#s" x="32"/><use href="#s" x="48"/><use href="#s" x="64"/></svg></div>
  </div>
  <div class="quote" style="left:776px">
    <div class="quote-who"><span class="avatar" role="img" aria-label="Portrait photo of the reviewer"></span><div><div class="quote-name">Nolan Brecker</div><div class="quote-role">Lorem Ipsum</div></div></div>
    <p>Lorem Ipsum is simply dummy text of the printing and typesetting industry. Lorem Ipsum has been the industry's standard dummy text ever since the 1500s, when an unknown printer took a galley of type and scrambled it to make a type specimen book.</p>
    <div class="stars"><svg width="80" height="14" viewBox="0 0 80 14" fill="#c9a14a"><use href="#s"/><use href="#s" x="16"/><use href="#s" x="32"/><use href="#s" x="48"/><use href="#s" x="64"/></svg></div>
  </div>
</section>

<section class="partners" aria-label="Partners">
  <span class="partner"></span><span class="partner"></span><span class="partner"></span><span class="partner"></span><span class="partner"></span><span class="partner"></span>
</section>

<footer class="site-footer">
  <div class="abs foot-col" style="left:220px;top:110px">
    <h4>Quick Links</h4>
    <ul class="foot-links"><li>Home</li><li>About Us</li><li>Office Rental</li><li>Home rental</li><li>Our Blog</li><li>Contact Us</li></ul>
  </div>
  <span class="foot-divider" style="left:420px"></span>
  <span class="foot-divider" style="left:780px"></span>
  <div class="foot-brand">
    <span class="brand-mark"></span>
    <div class="brand-name" style="font-size:16px">Birch Spire Kilo Marsh</div>
    <div class="social"><span></span><span></span><span></span></div>
  </div>
  <div class="abs foot-col" style="left:820px;top:110px;width:190px;text-align:right">
    <h4>Contact Us</h4>
    <ul class="contact">
      <li>+1 (555) 014-2280<span class="ico"><svg width="14" height="14" viewBox="0 0 14 14"><path d="M3 1l2.5 3-1.5 1.5a8 8 0 0 0 4.5 4.5L10 8.5l3 2.5-1.5 2C6 13 1 8 1 2.5z" fill="#1b1b1b"/></svg></span></li>
      <li>hello@birchspire-km.com<span class="ico"><svg width="14" height="12" viewBox="0 0 14 12"><rect x=".5" y=".5" width="13" height="11" fill="none" stroke="#1b1b1b"/><path d="M.5 .5 7 6l6.5-5.5" fill="none" stroke="#1b1b1b"/></svg></span></li>
      <li>88 Larchmont Avenue,<br>Harlow Ridge 40512<span class="ico"><svg width="12" height="14" viewBox="0 0 12 14"><path d="M6 13S1 8 1 5a5 5 0 0 1 10 0c0 3-5 8-5 8z" fill="#1b1b1b"/><circle cx="6" cy="5" r="1.8" fill="#fff"/></svg></span></li>
    </ul>
  </div>
</footer>
<div class="copyright">© Copyright 2024 Birch Spire Kilo Marsh - All rights reserved</div>

</body>
</html>
```